Business Card and Letterhead Design for Public Accounting Firm

Business card and letterhead design for a CPA Firm located in Orange County, CA. We're looking for a modern and professional design utilizing our existing logo. We'd like a clean "less is more" look, but also something that catches the eye. We provide a high level of service to our clients. Open to single or double sided business cards.

Additional info: color numbers on logo
Blue :
R 0
G 83
B 125

#00537D

Silver :

R 154
G 154
B 154

#9A9A9A

Target Market(s)

Businesses and individuals

Industry/Entity Type

Accounting

Contact Information for Business Card

Moss Whitfield & Danby LLP - 4827 Larkspur Vale Road, Irvine, CA 92614 - (949)731-2864 - mwdaccts.example

Font styles to use
Serif
Sans Serif
Other font styles liked:
• See font file uploaded

Colors
0054AA
0677BA
7BADD7
CADEEF
E8F1F8

Requirements
Nice to have
• Possibly use the font file provided which matches our logo, but adjust to be not in all caps

```html
<!DOCTYPE html>
<html lang="en">
<head>
<meta charset="utf-8">
<title>Moss Whitfield &amp; Danby LLP — Stationery</title>
<link rel="stylesheet" href="https://fonts.googleapis.com/css2?family=Libre+Baskerville:wght@400;700&display=swap">
<style>
  :root {
    --brand-blue: #00537d;
    --brand-silver: #9a9a9a;
    --backdrop: #959595;
    --paper: #ffffff;
    --rule: #8f8f8f;
    --watermark: #f1f1f1;
    --card-mark: #0b4566;
  }
  * { margin: 0; padding: 0; box-sizing: border-box; }
  html, body { width: 1200px; height: 1000px; overflow: hidden; }
  body {
    background: var(--backdrop);
    font-family: "Libre Baskerville", Georgia, serif;
    position: relative;
  }

  /* Letterhead */
  .letterhead {
    position: absolute; left: 505px; top: 85px;
    width: 594px; height: 840px;
    background: var(--paper);
    box-shadow: 0 3px 10px rgba(0,0,0,0.25);
  }
  .letterhead__brand {
    position: absolute; left: 40px; top: 34px;
    display: flex; align-items: center; gap: 10px;
  }
  .brand-dot {
    width: 14px; height: 14px; border-radius: 50%;
    background: var(--brand-blue);
  }
  .brand-name {
    color: var(--brand-blue);
    font-size: 15px; line-height: 19px; letter-spacing: 0.5px;
  }
  .letterhead__address {
    position: absolute; right: 35px; top: 43px;
    text-align: right; color: var(--brand-silver);
    font-size: 14.5px; line-height: 19px;
  }
  .letterhead__watermark {
    position: absolute; left: 0; right: 0; top: 385px;
    text-align: center; color: var(--watermark);
    font-size: 46px; line-height: 56px;
  }
  .letterhead__rule {
    position: absolute; left: 26px; right: 35px; top: 771px;
    border-top: 1px solid var(--rule);
  }
  .letterhead__phone {
    position: absolute; left: 26px; top: 796px;
    color: var(--brand-silver); font-size: 14px; font-weight: 700;
  }
  .letterhead__web {
    position: absolute; right: 35px; top: 795px;
    color: var(--brand-silver); font-size: 15px;
  }
  .web-domain { color: var(--brand-blue); font-weight: 700; }

  /* Business cards */
  .card {
    position: absolute; left: 138px;
    width: 277px; height: 158px; border-radius: 12px;
    box-shadow: 0 2px 6px rgba(0,0,0,0.25);
  }
  .card--front {
    top: 349px; background: var(--brand-blue);
    display: flex; align-items: center; justify-content: center;
  }
  .card--front .brand-name { color: var(--card-mark); font-size: 13px; line-height: 16px; }
  .card--back { top: 539px; background: var(--paper); }
  .card__brand {
    position: absolute; left: 17px; top: 30px;
    color: var(--brand-blue); font-size: 10px; letter-spacing: 0.3px;
  }
  .card__firm {
    position: absolute; left: 17px; top: 66px;
    color: var(--brand-blue); font-size: 7px; font-weight: 700;
  }
  .card__address {
    position: absolute; left: 17px; top: 88px;
    color: #7a7a7a; font-size: 6.5px; line-height: 10px;
  }
  .card__rule {
    position: absolute; left: 17px; right: 20px; top: 122px;
    border-top: 1px solid #b5b5b5;
  }
  .card__phone {
    position: absolute; left: 17px; top: 130px;
    color: #7a7a7a; font-size: 6.5px;
  }
  .card__web {
    position: absolute; right: 20px; top: 128px;
    color: var(--brand-silver); font-size: 7px;
  }
</style>
</head>
<body>

  <section class="card card--front" aria-label="Business card front">
    <div class="brand-name">Moss Whitfield &amp; Danby LLP</div>
  </section>

  <section class="card card--back" aria-label="Business card back">
    <div class="card__brand">Moss Whitfield &amp; Danby LLP</div>
    <div class="card__firm">Moss Whitfield &amp; Danby LLP</div>
    <div class="card__address">4827 Larkspur Vale Road<br>Irvine, CA 92614</div>
    <div class="card__rule"></div>
    <div class="card__phone">(949) 731-2864</div>
    <div class="card__web"><span class="web-domain">mwdaccts</span>.example</div>
  </section>

  <section class="letterhead" aria-label="Letterhead">
    <div class="letterhead__brand">
      <span class="brand-dot"></span>
      <div class="brand-name">Moss Whitfield<br>&amp; Danby LLP</div>
    </div>
    <div class="letterhead__address">4827 Larkspur Vale Road<br>Irvine, CA 92614</div>
    <div class="letterhead__watermark">Moss Whitfield<br>&amp; Danby</div>
    <div class="letterhead__rule"></div>
    <div class="letterhead__phone">(949) 731-2864</div>
    <div class="letterhead__web"><span class="web-domain">mwdaccts</span>.example</div>
  </section>

</body>
</html>
```